The Seeds Beneath Wintermoor Inc.

On one side have the business name. On the other side have contact information. This is an indoor cannabis cultivation business. It’s a new company in Sacramento ca. So we need a logo designed. The company is Called the seeds beneath wintermoor. We grow and distribute marijuana in California. We would like to see designers use the color green and communicate cultivation.

Target Market(s)

Networking

Contact Information for Business Card

Wade Tirrenbek: president
Phone: (916) 555-0173
Email: wade@theseedsbeneathwintermoor.net

Logo Text

Not sure if i want text or just an image created by designers.

Font styles to use
Script

Colors
000000
9bcb3c
fbfcf7
cadf82

Requirements
Nice to have
• A classic elegant professional card.

```html
<!DOCTYPE html>
<html lang="en">
<head>
<meta charset="utf-8">
<title>The Seeds Beneath Wintermoor Inc. — Business Card</title>
<link rel="stylesheet" href="https://fonts.googleapis.com/css2?family=Mulish:wght@400;800&display=swap">
<style>
  :root {
    --black: #000000;
    --green: #9bcb3c;
    --paper: #f3f3f1;
    --ink-grey: #4a4a4a;
    --backdrop: #1c1c1c;
    --white: #fbfcf7;
  }
  * { margin: 0; padding: 0; box-sizing: border-box; }
  html, body {
    width: 1131px; height: 1200px; overflow: hidden;
    background: var(--backdrop);
    font-family: "Mulish", "Avenir", sans-serif;
  }
  .canvas { position: relative; width: 1131px; height: 1200px; }
  .card {
    position: absolute; left: 153px; width: 781px; height: 447px;
    border-radius: 22px; overflow: hidden;
  }
  .card--front { top: 109px; background: var(--paper); }
  .card--back { top: 599px; background: var(--green); }

  .brand { position: absolute; text-align: center; }
  .brand__mark { display: flex; align-items: center; justify-content: center; gap: 10px; }
  .brand__dot { border-radius: 50%; }
  .brand__name { font-weight: 800; color: var(--black); letter-spacing: 1px; line-height: 1; }
  .brand__tagline { color: var(--ink-grey); font-weight: 400; white-space: nowrap; }

  .card--front .brand { left: 66px; top: 170px; width: 272px; }
  .card--front .brand__dot { width: 22px; height: 22px; background: var(--green); }
  .card--front .brand__name { font-size: 56px; }
  .card--front .brand__tagline { font-size: 17px; margin-top: 14px; }

  .divider {
    position: absolute; left: 356px; top: 148px; width: 1px; height: 159px;
    background: var(--green);
  }
  .contact { position: absolute; left: 390px; top: 144px; color: var(--ink-grey); }
  .contact__name { font-size: 32px; color: var(--green); font-weight: 400; line-height: 1.1; white-space: nowrap; }
  .contact__role { font-size: 16px; margin-top: 4px; }
  .contact__list { list-style: none; margin-top: 23px; }
  .contact__item { display: flex; align-items: center; gap: 12px; font-size: 16px; height: 27.5px; white-space: nowrap; }
  .contact__icon { width: 12px; height: 12px; fill: var(--green); flex: none; }

  .band {
    position: absolute; left: 0; top: 394px; width: 100%; height: 24px;
    background: var(--green);
  }
  .band__chevron { position: absolute; left: 232px; top: 0; }

  .card--back .brand { left: 0; top: 178px; width: 100%; }
  .card--back .brand__dot { width: 34px; height: 34px; background: var(--white); }
  .card--back .brand__name { font-size: 96px; }
  .card--back .brand__tagline { font-size: 31px; margin-top: 26px; }
</style>
</head>
<body>
<main class="canvas">
  <section class="card card--front" aria-label="Card front">
    <div class="brand">
      <div class="brand__mark"><span class="brand__dot"></span><span class="brand__name">TSBW</span></div>
      <p class="brand__tagline">the seeds beneath wintermoor</p>
    </div>
    <div class="divider"></div>
    <div class="contact">
      <h1 class="contact__name">Wade Tirrenbek</h1>
      <p class="contact__role">president</p>
      <ul class="contact__list">
        <li class="contact__item">
          <svg class="contact__icon" viewBox="0 0 24 24"><path d="M6.6 10.8a15.1 15.1 0 0 0 6.6 6.6l2.2-2.2c.3-.3.7-.4 1-.2 1.1.4 2.3.6 3.6.6.6 0 1 .4 1 1V20c0 .6-.4 1-1 1A17 17 0 0 1 3 4c0-.6.4-1 1-1h3.5c.6 0 1 .4 1 1 0 1.3.2 2.5.6 3.6.1.3 0 .7-.2 1z"/></svg>
          <span>(916) 555-0173</span>
        </li>
        <li class="contact__item">
          <svg class="contact__icon" viewBox="0 0 24 24"><path d="M2 8c3-4 17-4 20 0l-1 3-4-1V8c-3-1-7-1-10 0v2l-4 1zM6 12h12l3 4v5H3v-5zm6 2a3 3 0 1 0 0 6 3 3 0 0 0 0-6z"/></svg>
          <span>(916) 555-0173</span>
        </li>
        <li class="contact__item">
          <svg class="contact__icon" viewBox="0 0 24 24"><path d="M2 5h20v2l-10 6L2 7zm0 4l10 6 10-6v10H2z"/></svg>
          <span>wade@theseedsbeneathwintermoor.net</span>
        </li>
      </ul>
    </div>
    <div class="band">
      <svg class="band__chevron" width="16" height="24" viewBox="0 0 16 24"><path d="M3 1l10 11-10 11" fill="none" stroke="var(--white)" stroke-width="3"/></svg>
    </div>
  </section>

  <section class="card card--back" aria-label="Card back">
    <div class="brand">
      <div class="brand__mark"><span class="brand__dot"></span><span class="brand__name">TSBW</span></div>
      <p class="brand__tagline">the seeds beneath wintermoor</p>
    </div>
  </section>
</main>
</body>
</html>
```